SEO AND WEB DESIGN COMPANY BUSINESS CARD DESIGN

I need an eye catching , simple business card design that will match my logo . I need 2 versions of it ( white background and black background) - SOME PEOPLE DID NOT GET IT AND SENDING US FRONT WHITE BACK WHITE VERSIONS WHICH IS NOT CORRECT.

ONE VERSION SHOULD BE BACK AND FRONT ALL BLACK , SECOND VERSION SHOULD BE BACK AND FRONT ALL WHITE

logo psd files are attached for both versions. The business card is going to have : First Name- Last name - position - phone numbers

```html
<!DOCTYPE html>
<html lang="en">
<head>
<meta charset="utf-8">
<title>Northpeak Digital — Business Cards</title>
<link rel="stylesheet" href="https://fonts.googleapis.com/css2?family=Lato:wght@400;700&family=Oswald:wght@600&display=swap">
<style>
  :root {
    --backdrop: #121314;
    --card: #1d1e20;
    --accent: #3a8ef0;
    --ink: #ffffff;
    --ink-soft: #e6e6e6;
  }
  * { margin: 0; padding: 0; box-sizing: border-box; }
  html, body { width: 1200px; height: 912px; overflow: hidden; }
  body {
    background: var(--backdrop);
    font-family: "Lato", Arial, sans-serif;
    position: relative;
  }
  .card {
    position: absolute;
    width: 620px;
    height: 354px;
    background: var(--card);
    box-shadow: 0 18px 40px rgba(0,0,0,0.55);
    overflow: hidden;
  }
  .card--front { left: 70px; top: 60px; }
  .card--back  { left: 510px; top: 498px; }

  .brand {
    display: flex;
    align-items: center;
    gap: 14px;
    position: absolute;
  }
  .brand__dot {
    border-radius: 50%;
    background: var(--accent);
    flex: none;
  }
  .brand__name {
    font-family: "Oswald", "Arial Narrow", sans-serif;
    font-weight: 600;
    color: var(--ink);
    text-transform: uppercase;
    letter-spacing: 0.02em;
    line-height: 1;
    white-space: nowrap;
  }
  .card--front .brand { left: 50%; top: 50%; transform: translate(-50%, -50%); }
  .card--front .brand__dot { width: 44px; height: 44px; }
  .card--front .brand__name { font-size: 54px; }

  .card--back .brand { left: 34px; top: 190px; gap: 9px; }
  .card--back .brand__dot { width: 22px; height: 22px; }
  .card--back .brand__name { font-size: 25px; }

  .divider {
    position: absolute;
    left: 312px;
    top: 150px;
    width: 1.5px;
    height: 104px;
    background: var(--accent);
  }
  .contact {
    position: absolute;
    left: 340px;
    top: 150px;
  }
  .contact__name {
    color: var(--accent);
    font-weight: 700;
    font-size: 27px;
    letter-spacing: -0.01em;
  }
  .contact__role {
    color: var(--ink-soft);
    font-size: 17px;
    margin-top: 4px;
  }
  .contact__phone {
    display: flex;
    align-items: center;
    gap: 10px;
    color: var(--ink-soft);
    font-size: 19px;
    margin-top: 14px;
    padding-left: 22px;
  }
  .contact__phone svg { width: 16px; height: 16px; fill: var(--accent); }
  .card__band {
    position: absolute;
    left: 0; right: 0; bottom: 0;
    height: 10px;
    background: var(--accent);
  }
</style>
</head>
<body>
  <section class="card card--front" aria-label="Card front">
    <div class="brand">
      <span class="brand__dot"></span>
      <span class="brand__name">Northpeak Digital</span>
    </div>
  </section>

  <section class="card card--back" aria-label="Card back">
    <div class="brand">
      <span class="brand__dot"></span>
      <span class="brand__name">Northpeak Digital</span>
    </div>
    <div class="divider"></div>
    <div class="contact">
      <p class="contact__name">Ellis Hartwell</p>
      <p class="contact__role">Manager</p>
      <p class="contact__phone">
        <svg viewBox="0 0 24 24" aria-hidden="true"><path d="M6.6 10.8a15.1 15.1 0 0 0 6.6 6.6l2.2-2.2c.3-.3.7-.4 1-.2 1.1.4 2.3.6 3.6.6.6 0 1 .4 1 1V20c0 .6-.4 1-1 1A17 17 0 0 1 3 4c0-.6.4-1 1-1h3.5c.6 0 1 .4 1 1 0 1.3.2 2.5.6 3.6.1.3 0 .7-.2 1z"/></svg>
        <span>555 014 2730</span>
      </p>
    </div>
    <div class="card__band"></div>
  </section>
</body>
</html>
```